Website Wordpress Responsive Design and Development - Landscape Company

Site is currently under construction, but the old site needs a refresh.
Need a fully responsive wordpress website (built in Elementor or comparable theme).
Here's the way it looked prior :
https://oldpages.example/snap/20220330041341/http://tobbsmaplegrove.example/
Their current designer came up with a website sample and it looks terrible :
https://danwelkerimages.sitebuild.example/mysite/projects
Websites the client likes for some inspiration, but needs better than these :
https://www.corwentlandscapearchitects.example/
http://qvateliernj.example/
https://brackenpartners.example/
https://www.tallanbysinc.example/

Navigation includes :
• Home
• Complete structure of website content is available in the home page, yielding main information on services.
• Visually appealing but simple to use and navigate. Subtle amount of content, but enough for search engines to be able to read up the target phrases.
• Sections on the home page include :
▪ About - Information about the company and main service focus
▪ Gallery - Imagery categorized to include lightbox style zoom.
▪ Contact - Contact details and connection information
• About
• Bannered header
• Content appropriately formatted to subject
• Gallery
• Bannered header
• Each of the albums would have their own categorized image content
• Contact
• Bannered header
• Social Media connector available on all pages (like box, feed, etc) if applicable
• Content can be updated on all pages
• Basic Optimization for SEO with title tags, meta data where applicable.
• Vantora Metrics and Sitemap installed. (vantora account will be provided)
• Vantora Firm Directory and Crawl Desk Accounts created

```html
<!DOCTYPE html>
<html lang="en">
<head>
<meta charset="utf-8">
<title>Tobb's Maplegrove, Inc — Mobile Screens</title>
<link rel="stylesheet" href="https://fonts.googleapis.com/css2?family=Heebo:wght@300;400;500&family=Montserrat:wght@400;600&display=swap">
<style>
  :root {
    --backdrop: #e9e9e9;
    --screen-dark: #1e1e1e;
    --paper: #ffffff;
    --ink: #1c1c1c;
    --heading: #474747;
    --accent-green: #4fc35c;
    --on-photo: #ffffff;
    --sky: #9db3c7;
    --sky-light: #c4d0da;
    --tree-dark: #1f3d1f;
    --tree: #2f5a2c;
    --lawn: #4f8a2a;
    --shrub-yellow: #a9a83a;
    --path: #7d7466;
    --wall-cream: #d8cfc4;
    --wall-mauve: #6f6570;
    --stone: #b9ad98;
    --apron: #2b2b2b;
  }
  * { box-sizing: border-box; margin: 0; padding: 0; }
  html, body {
    width: 1200px;
    height: 1200px;
    overflow: hidden;
    background: var(--backdrop);
  }
  .canvas {
    position: relative;
    width: 1200px;
    height: 1200px;
  }
  .screen {
    position: absolute;
    overflow: hidden;
    border-radius: 30px;
    background: var(--paper);
    box-shadow: 0 18px 40px rgba(0,0,0,0.14);
  }
  .screen--portfolio {
    left: 200px; top: 215px; width: 298px; height: 765px;
    background: var(--screen-dark);
  }
  .screen--about {
    left: 640px; top: 155px; width: 340px; height: 890px;
  }
  .photo { position: absolute; display: block; }
  .photo--garden {
    inset: 0;
    background: linear-gradient(180deg,
      #6f8296 0%, var(--sky) 12%, var(--sky-light) 20%, #8fa3b4 28%,
      #3c5a34 34%, var(--tree-dark) 44%, var(--tree) 54%,
      var(--lawn) 64%, #6f8f2e 72%, var(--shrub-yellow) 80%,
      var(--path) 88%, #5e6a2c 100%);
  }
  .photo-shade {
    position: absolute; inset: 0;
    background: linear-gradient(180deg, rgba(0,0,0,0.28) 0%, rgba(0,0,0,0.05) 35%, rgba(0,0,0,0.1) 65%, rgba(0,0,0,0.4) 100%);
  }
  .photo--house {
    left: 0; top: 0; width: 100%; height: 292px;
    background: linear-gradient(180deg,
      #7f9ab3 0%, #a9b9c8 18%, var(--wall-cream) 34%, #bdb2a8 46%,
      var(--wall-mauve) 60%, #5b5560 72%, #6d7d4a 84%, var(--lawn) 100%);
  }
  .photo--gardener {
    left: 43px; top: 606px; width: 250px; height: 284px;
    background: linear-gradient(180deg,
      #5f7a3c 0%, #86995a 18%, var(--stone) 40%, #a3977f 52%,
      var(--apron) 66%, #4a4a42 76%, #5d8a34 88%, var(--lawn) 100%);
  }
  .site-header {
    position: absolute;
    left: 18px; right: 18px;
    display: flex;
    align-items: center;
    justify-content: space-between;
  }
  .screen--portfolio .site-header { top: 42px; }
  .screen--about .site-header { top: 30px; }
  .brand {
    font-family: 'Heebo', sans-serif;
    font-weight: 400;
    font-size: 18px;
    color: var(--on-photo);
    letter-spacing: 0.2px;
  }
  .screen--about .brand { font-size: 20px; }
  .menu-icon { width: 26px; height: 22px; }
  .portfolio-arrow {
    position: absolute; left: 160px; top: 505px; width: 12px; height: 12px;
  }
  .hero-caption {
    position: absolute;
    left: 20px; top: 548px;
    font-family: 'Heebo', sans-serif;
    font-weight: 300;
    font-size: 28px;
    line-height: 36px;
    color: var(--on-photo);
  }
  .hero-caption .section-label { color: var(--accent-green); }
  .about {
    position: absolute;
    left: 50px; top: 340px; width: 275px;
  }
  .about-title {
    font-family: 'Montserrat', sans-serif;
    font-weight: 600;
    font-size: 20px;
    color: var(--heading);
    margin-bottom: 22px;
  }
  .about-text {
    font-family: 'Montserrat', sans-serif;
    font-weight: 400;
    font-size: 13.2px;
    line-height: 25px;
    color: var(--ink);
    white-space: nowrap;
  }
</style>
</head>
<body>
<div class="canvas">

  <section class="screen screen--portfolio">
    <div class="photo photo--garden" role="img" aria-label="Landscaped garden with paved path, shrubs, conifers and a bench"></div>
    <div class="photo-shade"></div>
    <header class="site-header">
      <span class="brand">Tobb's Maplegrove, Inc</span>
      <svg class="menu-icon" viewBox="0 0 26 22" aria-label="Menu">
        <g stroke="#fff" stroke-width="2" stroke-linecap="round">
          <line x1="1" y1="3" x2="16" y2="3"/>
          <line x1="1" y1="11" x2="22" y2="11"/>
          <line x1="1" y1="19" x2="25" y2="19"/>
        </g>
      </svg>
    </header>
    <svg class="portfolio-arrow" viewBox="0 0 12 12" aria-label="Next">
      <g stroke="#fff" stroke-width="1" fill="none" stroke-linecap="round">
        <line x1="1" y1="6" x2="11" y2="6"/>
        <polyline points="7,2 11,6 7,10"/>
      </g>
    </svg>
    <h1 class="hero-caption"><span class="section-label">Portfolio</span> |<br>Landscaping house</h1>
  </section>

  <section class="screen screen--about">
    <div class="photo photo--house" role="img" aria-label="Two-storey modern house with landscaped front garden"></div>
    <header class="site-header">
      <span class="brand">Tobb's Maplegrove, Inc</span>
      <svg class="menu-icon" viewBox="0 0 26 22" aria-label="Menu">
        <g stroke="#fff" stroke-width="2" stroke-linecap="round">
          <line x1="1" y1="3" x2="16" y2="3"/>
          <line x1="1" y1="11" x2="22" y2="11"/>
          <line x1="1" y1="19" x2="25" y2="19"/>
        </g>
      </svg>
    </header>
    <article class="about">
      <h2 class="about-title">ABOUT US</h2>
      <p class="about-text">Lorem ipsum dolor sit amet,<br>consectetur adipiscing elit. Egestas<br>nisl cum porta faucibus aliquam eget<br>enim, nulla. A metus gravida massa<br>arcu. Urna praesent venenatis sapien,<br>dignissim sed enim mi purus dolor.<br>Cursus turpis mus lectus orci arcu.<br>Risus vitae viverra tincidunt.</p>
    </article>
    <div class="photo photo--gardener" role="img" aria-label="Gardener in an apron pushing a lawn mower in a garden"></div>
  </section>

</div>
</body>
</html>
```